KVT Business Cards

We require business cards for our business. We would like a matte black back to the card, with our logo centred in the middle. The front side of the card is open to design.

Target Market(s)

Clients looking for legal services (professional)

Industry/Entity Type

Legal

Contact Information for Business Card

Boris Telemark
Partner
Mobile: 0438 715 642
Email: boris@kvtlaw.co
Website: www.kvtlaw.co
Level 3, 118 Wexbury Street
Sydney NSW 2000

Font styles to use
Other font styles liked:
• Avenir

Colors
f04a50
ffffff
1b1b1b

Requirements
Must have
• Black back with logo included in the centre of the card.
• Our font is Avenir.

```html
<!DOCTYPE html>
<html lang="en">
<head>
<meta charset="utf-8">
<title>KVT Business Cards</title>
<link rel="stylesheet" href="https://fonts.googleapis.com/css2?family=Montserrat:wght@400;500;700&display=swap">
<style>
  :root {
    --brand-red: #f04a50;
    --ink-black: #1b1b1b;
    --paper-white: #ffffff;
    --backdrop: #ececec;
    --muted-text: #d9d9d9;
  }
  * { margin: 0; padding: 0; box-sizing: border-box; }
  html, body { width: 1200px; height: 900px; overflow: hidden; }
  body {
    background: var(--backdrop);
    font-family: "Montserrat", "Nunito Sans", sans-serif;
    position: relative;
  }
  .card {
    position: absolute;
    left: 340px;
    width: 520px;
    height: 297px;
    overflow: hidden;
    box-shadow: 0 10px 28px rgba(0,0,0,0.16);
  }
  .card-back { top: 90px; background: var(--ink-black); border: 2px solid var(--brand-red); }
  .card-front { top: 500px; background: var(--paper-white); }
  .card-shapes { position: absolute; inset: 0; width: 100%; height: 100%; }

  .brand-lockup {
    position: absolute;
    display: flex;
    align-items: center;
    gap: 14px;
  }
  .brand-mark {
    width: 38px; height: 38px;
    background: var(--brand-red);
    flex: none;
  }
  .brand-name {
    color: var(--paper-white);
    font-weight: 700;
    font-size: 14px;
    line-height: 1.1;
    letter-spacing: 0.3px;
    text-transform: uppercase;
  }
  .card-back .brand-lockup { left: 50%; top: 112px; transform: translateX(-50%); }
  .back-website {
    position: absolute;
    left: 0; right: 0; top: 212px;
    text-align: center;
    color: var(--paper-white);
    font-size: 15px;
    letter-spacing: 0.4px;
  }

  .card-front .brand-lockup { left: 40px; top: 150px; }
  .card-front .brand-mark { width: 32px; height: 32px; }
  .card-front .brand-name { font-size: 12px; }
  .office-address {
    position: absolute;
    left: 40px; top: 226px;
    color: var(--paper-white);
    font-size: 11px;
    line-height: 1.45;
  }
  .holder {
    position: absolute;
    right: 36px; top: 32px;
    display: flex;
    align-items: stretch;
    gap: 8px;
    text-align: right;
  }
  .holder-name {
    color: var(--brand-red);
    font-weight: 700;
    font-size: 22px;
    line-height: 1.05;
    text-transform: uppercase;
  }
  .holder-role {
    color: var(--ink-black);
    font-size: 22px;
    font-weight: 400;
    line-height: 1.05;
  }
  .holder-rule { width: 2px; background: var(--brand-red); }
  .contact-list {
    position: absolute;
    left: 330px; top: 120px;
    list-style: none;
    color: var(--ink-black);
    font-size: 11.5px;
  }
  .contact-list li { display: flex; align-items: center; gap: 7px; margin-bottom: 7px; }
  .contact-icon { width: 12px; height: 12px; flex: none; }
</style>
</head>
<body>

<section class="card card-back" aria-label="Card back">
  <svg class="card-shapes" viewBox="0 0 516 293" preserveAspectRatio="none" aria-hidden="true">
    <polygon points="516,22 482,52 482,150 516,182" fill="var(--brand-red)"/>
    <polygon points="0,118 34,148 34,246 0,276" fill="var(--brand-red)"/>
  </svg>
  <div class="brand-lockup">
    <span class="brand-mark"></span>
    <span class="brand-name">Kessler Varn<br>Thorpe Legal</span>
  </div>
  <p class="back-website">www.kvtlaw.co</p>
</section>

<section class="card card-front" aria-label="Card front">
  <svg class="card-shapes" viewBox="0 0 520 297" preserveAspectRatio="none" aria-hidden="true">
    <polygon points="0,0 170,0 410,297 0,297" fill="var(--ink-black)"/>
    <polyline points="170,0 410,297" fill="none" stroke="var(--brand-red)" stroke-width="2"/>
    <polyline points="0,0 170,0" fill="none" stroke="var(--brand-red)" stroke-width="2"/>
    <polyline points="1,0 1,297 410,297" fill="none" stroke="var(--brand-red)" stroke-width="2"/>
  </svg>

  <div class="holder">
    <div>
      <p class="holder-name">Boris Telemark</p>
      <p class="holder-role">Partner</p>
    </div>
    <span class="holder-rule"></span>
  </div>

  <ul class="contact-list">
    <li>
      <svg class="contact-icon" viewBox="0 0 12 12" aria-hidden="true"><circle cx="6" cy="6" r="6" fill="var(--brand-red)"/><path d="M3.6 3.2l1.2-.3.6 1.4-.7.5a4 4 0 0 0 1.5 1.5l.5-.7 1.4.6-.3 1.2C6 7.6 4.4 6 3.6 3.2z" fill="#fff"/></svg>
      0438 715 642
    </li>
    <li>
      <svg class="contact-icon" viewBox="0 0 12 12" aria-hidden="true"><circle cx="6" cy="6" r="6" fill="var(--brand-red)"/><circle cx="6" cy="6" r="3.2" fill="none" stroke="#fff" stroke-width=".8"/><path d="M2.8 6h6.4M6 2.8c-1.4 1.8-1.4 4.6 0 6.4M6 2.8c1.4 1.8 1.4 4.6 0 6.4" fill="none" stroke="#fff" stroke-width=".7"/></svg>
      www.kvtlaw.co
    </li>
    <li>
      <svg class="contact-icon" viewBox="0 0 12 12" aria-hidden="true"><circle cx="6" cy="6" r="6" fill="var(--brand-red)"/><rect x="3" y="4" width="6" height="4.2" fill="none" stroke="#fff" stroke-width=".8"/><path d="M3 4l3 2.3L9 4" fill="none" stroke="#fff" stroke-width=".8"/></svg>
      boris@kvtlaw.co
    </li>
  </ul>

  <div class="brand-lockup">
    <span class="brand-mark"></span>
    <span class="brand-name">Kessler Varn<br>Thorpe Legal</span>
  </div>
  <p class="office-address">Level 3, 118 Wexbury Street<br>Sydney NSW 2000</p>
</section>

</body>
</html>
```